Velter Labs - Mushroom Supplement Packaging

Our brand is called Velter Labs. I've added a couple different logos that you can use. We are creating a line up of Mushroom Supplement products. I will add the entire line-up of products here. I've added examples of other products and packaging shape types I can purchase. Give me different options for packaging that is minimalist and clean for this brand that makes it look really well made and clean and make people want to buy.

Product 1 Lions Mane 1g
Product 2 Cordyceps 1g
Product 3 Chaga 1g
Product 4 Turkey Tail 1g
Product 5 Reishi 1g
Product 6 Maitake 1g
Product 7 Shiitake 1g

Product 8 (Mix) Lions Mane 143mg
Cordyceps 143mg
Chaga 143mg
Turkey Tail 143mg
Reishi 143mg
Maitake 143mg
Shiitake 143mg

```html
<!DOCTYPE html>
<html lang="en">
<head>
<meta charset="utf-8">
<title>Velter Labs – Lions Mane Mushroom Label</title>
<link rel="stylesheet" href="https://fonts.googleapis.com/css2?family=Bebas+Neue&family=Montserrat:wght@300;400;500;800&display=swap">
<style>
  :root {
    --backdrop: #c6c6c6;
    --label-light: #f3ead3;
    --label-mid: #ddd0ac;
    --label-edge: #b9a97f;
    --ink: #2a1a12;
    --brand-green: #4f8a5d;
    --pill-text: #f3ead3;
  }
  * { margin: 0; padding: 0; box-sizing: border-box; }
  html, body {
    width: 1200px;
    height: 675px;
    overflow: hidden;
    background: var(--backdrop);
  }
  .canvas {
    position: relative;
    width: 1200px;
    height: 675px;
    display: flex;
    align-items: center;
    justify-content: center;
  }
  .label {
    position: relative;
    width: 540px;
    height: 610px;
    display: flex;
    flex-direction: column;
    align-items: center;
    color: var(--ink);
    font-family: "Montserrat", sans-serif;
  }
  .label-texture {
    position: absolute;
    inset: 0;
    background: radial-gradient(ellipse at 50% 40%, var(--label-light) 0%, var(--label-mid) 60%, var(--label-edge) 100%);
  }
  .label-content {
    position: relative;
    display: flex;
    flex-direction: column;
    align-items: center;
    width: 100%;
    height: 100%;
    padding-top: 50px;
  }
  .brand {
    display: flex;
    flex-direction: column;
    align-items: center;
    gap: 12px;
    height: 190px;
    justify-content: center;
  }
  .brand-dot {
    width: 40px;
    height: 40px;
    border-radius: 50%;
    background: var(--brand-green);
  }
  .brand-name {
    font-family: "Montserrat", sans-serif;
    font-weight: 800;
    font-size: 34px;
    letter-spacing: 2px;
    text-transform: uppercase;
    color: var(--brand-green);
  }
  .product-name {
    margin-top: 34px;
    font-family: "Bebas Neue", sans-serif;
    font-size: 118px;
    line-height: 0.9;
    letter-spacing: 1px;
  }
  .product-type {
    font-weight: 800;
    font-size: 30px;
    letter-spacing: 2px;
    margin-top: 6px;
  }
  .benefit {
    margin-top: 46px;
    font-weight: 400;
    font-size: 21px;
    line-height: 1.25;
    text-align: center;
    text-transform: uppercase;
  }
  .dose {
    margin-top: 22px;
    background: var(--ink);
    color: var(--pill-text);
    font-weight: 500;
    font-size: 24px;
    padding: 4px 16px 8px;
    border-radius: 10px;
  }
  .footer-line {
    margin-top: 30px;
    font-weight: 500;
    font-size: 16px;
    letter-spacing: 0.5px;
    text-transform: uppercase;
    display: flex;
    gap: 14px;
  }
</style>
</head>
<body>
  <main class="canvas">
    <section class="label">
      <div class="label-texture" role="img" aria-label="Cream wavy-line paper texture"></div>
      <div class="label-content">
        <div class="brand">
          <span class="brand-dot"></span>
          <span class="brand-name">Velter Labs</span>
        </div>
        <h1 class="product-name">LIONS MANE</h1>
        <p class="product-type">MUSHROOM</p>
        <p class="benefit">Brain and nervous system<br>health support</p>
        <p class="dose">1g per capsule</p>
        <p class="footer-line"><span>Herbal supplement</span><span>|</span><span>60 capsules</span></p>
      </div>
    </section>
  </main>
</body>
</html>
```